Award winning photographer needs a website.

I need a Plumleaf website that showcases my photos. I want them arranged via category, which might be a specific place or a theme. Here are categories I am thinking of:
1. Yarra Valley and Ranges
2. East coast Tasmania
3. Landscapes
4. Seascapes
5. Urban
6. Nepal
7. Macro
I need to be able to upload and download the photos myself. Currently, there is no need for this site to have an ecommerce component. I would like a blog page where I can post about my photographic adventures and maybe add some short videos of me on my way to the shoot, or of the people I meet. I also want to have it so that each photo has a title and if people click on a photo they can read a story about how I came to shoot it etc. There will also be my contact details and how to purchase a print which will happen through other communications. Like i mentioned, no e commerce at this point. I would like a page for awards as I have several. Here are some URLs of sites I like to give you some idea of what I'm looking at:

https://www.vendrimask.com/
https://tobyfarnellphotography.example/
https://www.maudelinskyphotography.example/

I can upload some images for you to start putting together someting if that hepls

Industry/Entity Type

Photography

Coding

Coded - Design and coding required

Number of Pages Required

5+ page

Font styles to use
Sans Serif

Requirements
Must have
• Multiple pages to display photos in different categories

```html
<!DOCTYPE html>
<html lang="en">
<head>
<meta charset="utf-8">
<title>Michael Thornbury Photography</title>
<link rel="stylesheet" href="https://fonts.googleapis.com/css2?family=Lora:wght@400;600&family=Open+Sans:wght@400;600&display=swap">
<style>
:root{
  --ink:#1b1b1b;
  --muted:#777;
  --paper:#ffffff;
  --night:#000000;
  --accent:#c8334a;
  --line:#e4e4e4;
  --navy:#2d3b55;
}
*{box-sizing:border-box;margin:0;padding:0}
html,body{width:1200px;height:2540px;overflow:hidden;background:var(--paper)}
body{font-family:"Open Sans",sans-serif;color:var(--ink);position:relative}
.wrap{width:792px;margin:0 auto;position:relative}

/* header */
.site-header{height:48px;position:relative;z-index:5;background:var(--paper)}
.site-header .wrap{display:flex;align-items:center;height:48px}
.brand{font-family:"Lora",serif;font-size:13px;font-weight:600;line-height:1;color:var(--ink);width:264px}
.brand small{display:block;font-size:7px;letter-spacing:2px;font-weight:600;margin-top:3px}
.main-nav{display:flex;gap:22px;font-size:11px;position:relative}
.main-nav a{color:var(--ink);text-decoration:none}
.main-nav .is-open{background:var(--accent);color:#fff;padding:4px 10px}
.dropdown{position:absolute;left:0;top:22px;width:150px;background:#fff;box-shadow:0 4px 14px rgba(0,0,0,.15);padding:10px 14px;list-style:none}
.dropdown li{font-size:9px;padding:5px 0;border-bottom:1px solid var(--line)}
.dropdown li:last-child{border:0}
.header-icons{margin-left:auto;display:flex;gap:14px;align-items:center}
.dot-icon{width:10px;height:10px;border-radius:50%;background:var(--ink)}

/* hero */
.hero{height:504px;position:relative;background:linear-gradient(180deg,#3b3f7a 0%,#9a6fa8 32%,#e3a2b4 48%,#4f6a48 62%,#24361f 100%);display:flex;flex-direction:column;align-items:center;justify-content:center;color:#fff}
.hero-name{font-family:"Lora",serif;font-size:72px;line-height:1;margin-top:40px;text-shadow:0 2px 8px rgba(0,0,0,.3)}
.hero-tag{font-size:12px;letter-spacing:6px;margin-top:8px}

/* about */
.about{height:244px;padding:44px 0 0}
.about .wrap{display:flex;gap:30px}
.about-text{width:370px}
.section-title{font-family:"Lora",serif;font-weight:400;color:var(--navy);font-size:32px;margin-bottom:14px}
.about-text p{font-size:10px;line-height:1.7;color:var(--muted);margin-bottom:8px}
.video{width:392px;height:168px;background:linear-gradient(135deg,#3a3a3a,#8b8e94 60%,#2a2a2a);position:relative}
.video-bar{position:absolute;left:0;right:0;bottom:0;height:22px;background:rgba(0,0,0,.6);display:flex;align-items:center;padding:0 10px;gap:10px}
.video-bar .track{flex:1;height:3px;background:#888}

/* collections */
.collections{background:var(--night);color:#fff;padding:34px 0 0;height:732px;overflow:hidden}
.collections h2{font-family:"Lora",serif;font-weight:400;font-size:36px;line-height:1.2;text-align:center}
.filters{display:flex;gap:16px;font-size:9px;margin:14px 0 12px}
.filters span:first-child{color:var(--accent)}
.grid{display:grid;grid-template-columns:250px 250px 268px;gap:12px;align-items:start}
.col{display:flex;flex-direction:column;gap:12px}
.ph{position:relative}
.ph-label{position:absolute;left:0;right:0;top:46%;text-align:center;font-family:"Lora",serif;font-size:14px}

/* blog */
.blog{padding:54px 0 0;height:540px;overflow:hidden}
.blog h2{font-family:"Lora",serif;font-weight:400;font-size:38px;line-height:1.25;text-align:center;width:560px;margin:0 auto 56px}
.cards{display:flex;gap:24px}
.card{width:248px}
.card-img{height:160px;margin-bottom:18px}
.card h3{font-family:"Lora",serif;font-weight:600;font-size:14px;line-height:1.35;margin-bottom:12px}
.meta{font-size:8px;color:var(--muted);display:flex;gap:16px}

/* contact */
.contact{background:var(--night);color:#fff;padding:44px 0 0;height:356px}
.contact h2{font-family:"Lora",serif;font-weight:400;font-size:28px;margin-bottom:12px}
.contact p{font-size:9px;line-height:1.6;color:#ccc;width:720px;margin-bottom:22px}
.form{display:flex;gap:20px}
.fields{display:flex;flex-direction:column;gap:8px;width:380px}
.field{height:24px;background:#fff}
.btn{width:60px;height:22px;background:var(--accent);color:#fff;font-size:9px;display:flex;align-items:center;justify-content:center}
.message{flex:1;height:112px;background:#fff}

/* footer */
.site-footer{padding:28px 0 0;height:116px}
.footer-row{display:flex;align-items:center;padding-bottom:30px;border-bottom:1px solid var(--line)}
.footer-links{margin-left:auto;display:flex;gap:16px;font-size:9px;margin-right:160px}
.footer-social{display:flex;gap:14px}
.copy{font-size:8px;color:var(--muted);padding:12px 0}
</style>
</head>
<body>

<header class="site-header">
  <div class="wrap">
    <div class="brand">Michael Thornbury<small>PHOTOGRAPHY</small></div>
    <nav class="main-nav">
      <a class="is-open" href="#">Collections ▾</a>
      <a href="#">Awards</a>
      <a href="#">Blog</a>
      <ul class="dropdown">
        <li>Yarra Valley and Ranges</li>
        <li>East Coast Tasmania</li>
        <li>Landscapes</li>
        <li>Seascapes</li>
        <li>Urban</li>
        <li>Nepal</li>
        <li>Macro</li>
      </ul>
    </nav>
    <div class="header-icons">
      <span class="dot-icon"></span><span class="dot-icon"></span>
      <svg width="11" height="11" viewBox="0 0 12 12"><circle cx="5" cy="5" r="3.6" fill="none" stroke="#1b1b1b" stroke-width="1.4"/><line x1="7.6" y1="7.6" x2="11" y2="11" stroke="#1b1b1b" stroke-width="1.4"/></svg>
    </div>
  </div>
</header>

<section class="hero" role="img" aria-label="Country road winding through green fields under a purple sunset sky">
  <div class="hero-name">Michael Thornbury</div>
  <div class="hero-tag">PHOTOGRAPHY</div>
</section>

<section class="about">
  <div class="wrap">
    <div class="about-text">
      <h2 class="section-title">About Michael</h2>
      <p>Michael Thornbury is an award winning photographer based in Melbourne who loves the wild coasts, quiet valleys and high peaks of Australia and beyond. Each image tells a story of patience, early starts and chasing light.</p>
      <p>Through his lens he shares moments from remote landscapes, busy streets and tiny worlds seen up close.</p>
    </div>
    <div class="video" role="img" aria-label="Short video of the photographer standing inside a building">
      <div class="video-bar">
        <svg width="8" height="9" viewBox="0 0 8 9"><path d="M0 0L8 4.5L0 9Z" fill="#fff"/></svg>
        <div class="track"></div>
        <span style="font-size:8px;color:#fff">0:00</span>
      </div>
    </div>
  </div>
</section>

<section class="collections">
  <div class="wrap">
    <h2>My Collections</h2>
    <div class="filters"><span>All</span><span>Seascape</span><span>Nepal</span><span>Panorama</span><span>Urban</span><span>Yarra Valley</span><span>Macro</span></div>
    <div class="grid">
      <div class="col">
        <div class="ph" style="height:128px;background:linear-gradient(180deg,#3b2a22,#d9772d 55%,#1b140f)" role="img" aria-label="Sunset over a rocky sea stack"></div>
        <div class="ph" style="height:236px;background:linear-gradient(160deg,#1a1f2a,#6e7a86 50%,#23201c)" role="img" aria-label="Misty sunrise seen through rocks"></div>
        <div class="ph" style="height:180px;background:linear-gradient(150deg,#4d3d1c,#b38a3a 50%,#2f2a14)" role="img" aria-label="Autumn forest path in golden light"></div>
      </div>
      <div class="col">
        <div class="ph" style="height:168px;background:linear-gradient(170deg,#2b2f3a,#a4553f 55%,#3a2b25)" role="img" aria-label="Orange lichen covered rocks on the coast"></div>
        <div class="ph" style="height:156px;background:linear-gradient(180deg,#3c5267,#7b8fa3 50%,#1d2733)" role="img" aria-label="Coastal rocks at dusk in Tasmania"><div class="ph-label">Tasmania</div></div>
        <div class="ph" style="height:128px;background:linear-gradient(180deg,#46295c,#c66f8d 55%,#2a1e2f)" role="img" aria-label="Pink sunset sky over a long road"></div>
      </div>
      <div class="col">
        <div class="ph" style="height:168px;background:linear-gradient(160deg,#222,#c7c7c7 50%,#333)" role="img" aria-label="Black and white snowy mountain range"></div>
        <div class="ph" style="height:156px;background:linear-gradient(180deg,#0c1224,#2c3f66 60%,#c9a054)" role="img" aria-label="City lights reflecting on water at night"></div>
        <div class="ph" style="height:196px;background:radial-gradient(circle at 50% 55%,#e04a86 0%,#a42258 38%,#000 62%)" role="img" aria-label="Close up of a pink flower on black"></div>
      </div>
    </div>
  </div>
</section>

<section class="blog">
  <div class="wrap">
    <h2>Read my blog to know about my photographic adventures</h2>
    <div class="cards">
      <article class="card">
        <div class="card-img" style="background:linear-gradient(180deg,#5c2a5a,#d8667a 50%,#3a1e22)" role="img" aria-label="Crimson sunset over a Tasmanian beach"></div>
        <h3>Tasmania: A Photographer's Paradise of Untamed Beauty</h3>
        <div class="meta"><span>June 14, 2023</span><span>Tasmania</span></div>
      </article>
      <article class="card">
        <div class="card-img" style="background:linear-gradient(180deg,#1b2a44,#5e6f8f 50%,#151a22)" role="img" aria-label="City skyline at blue hour"></div>
        <h3>Immersed in the Wonders of Urban-scapes: A Photographer's Journey</h3>
        <div class="meta"><span>June 13, 2023</span><span>Cityscape</span></div>
      </article>
      <article class="card">
        <div class="card-img" style="background:linear-gradient(160deg,#1e1e1e,#bdbdbd 50%,#2b2b2b)" role="img" aria-label="Black and white Himalayan peaks"></div>
        <h3>Capturing the Splendors of Nepal: A Photographer's Paradise</h3>
        <div class="meta"><span>June 12, 2023</span><span>Nepal</span></div>
      </article>
    </div>
  </div>
</section>

<section class="contact">
  <div class="wrap">
    <h2>Get in touch</h2>
    <p>For enquiries and to purchase captivating photographs by Michael Thornbury, please contact him through the contact form. Let him know the details of your space and create a sense of wonder and beauty.</p>
    <div class="form">
      <div class="fields">
        <div class="field"></div>
        <div class="field"></div>
        <div class="field"></div>
        <div class="btn">Send</div>
      </div>
      <div class="message"></div>
    </div>
  </div>
</section>

<footer class="site-footer">
  <div class="wrap">
    <div class="footer-row">
      <div class="brand">Michael Thornbury<small>PHOTOGRAPHY</small></div>
      <nav class="footer-links"><span>Collections</span><span>Awards</span><span>Blog</span></nav>
      <div class="footer-social"><span class="dot-icon"></span><span class="dot-icon"></span></div>
    </div>
    <div class="copy">© 2023 Michael Thornbury Photography. All Rights Reserved.</div>
  </div>
</footer>

</body>
</html>
```